Label Redesign For Hemp Oil Tincture Bottle*

I need a label redesigned for Marbleleaf Hemp, current bottle label and logo is attached. The current label doesn't standout, not sure if its the font size or colors on the existing label. It is very important to have on the label that this is a Premium Full Spectrum Hemp Oil that is 2000mg. Then after the label is redesigned and approved, I would need to packaging to be designed to match the approved label design.
This Hemp oil has a relaxing effect to help ease mental and emotional stress, tension and worry. The Omega Fatty Acids it contains also naturally improves your mood and overall brain function, causing you to feel more alert and focused. Hemp Oil helps with insomnia. Take some 2-3 hours before bedtime, you will feel relaxed yet aware of how tired you are that it will lead to a good night's sleep. Hemp Oil helps ease chronic pain and inflammation from conditions such as arthritis, fibromyalgia, lupus, and MS. As a pain relief supplement, it is a safer, natural, non-chemical and non-addictive alternative to prescription painkillers.

Target Market(s)

Adults

Industry/Entity Type

Supplement

Font styles to use
Serif
Sans Serif

Colors

Designer to choose colors to be used in the design.

Requirements
Must have
• All information thats on current label but where it says 750 in the front of the existing label, it needs to say 2000. The 2000 should be prominent on the label.

```html
<!DOCTYPE html>
<html lang="en">
<head>
<meta charset="utf-8">
<title>Marbleleaf Hemp – Tincture Label</title>
<link rel="stylesheet" href="https://fonts.googleapis.com/css2?family=Crimson+Text:wght@400;600&display=swap">
<style>
  :root {
    --page-bg: #ecebe8;
    --teal: #8fcdc3;
    --teal-light: #b4ded7;
    --silver: #d4d4d6;
    --silver-light: #f1f1f2;
    --gold: #d6a446;
    --ink: #1c1c1c;
    --white: #ffffff;
  }
  * { box-sizing: border-box; margin: 0; padding: 0; }
  html, body {
    width: 796px; height: 1200px; overflow: hidden;
    background: var(--page-bg);
    font-family: "Crimson Text", Georgia, serif;
  }
  .label {
    position: absolute; left: 28px; top: 100px;
    width: 740px; height: 1000px;
    box-shadow: 0 6px 24px rgba(0,0,0,.15);
    overflow: hidden;
  }
  .label__top {
    position: absolute; left: 0; top: 0; width: 100%; height: 420px;
    background: linear-gradient(90deg, var(--teal) 0%, var(--teal-light) 40%, var(--teal) 100%);
  }
  .label__bottom {
    position: absolute; left: 0; top: 420px; width: 100%; height: 580px;
    background: linear-gradient(90deg, var(--silver) 0%, var(--silver-light) 45%, var(--silver) 100%);
  }
  .label__rule {
    position: absolute; left: 0; top: 416px; width: 100%; height: 5px;
    background: var(--gold);
  }
  .brand-box {
    position: absolute; left: 250px; top: 20px; width: 260px; height: 210px;
    background: var(--white);
    border: 2px solid var(--gold);
    display: flex; flex-direction: column; align-items: center; justify-content: center;
    gap: 24px;
  }
  .brand-box__name {
    font-size: 30px; color: #5a5a5a; line-height: 1.1; text-align: center;
  }
  .brand-box__mark {
    width: 14px; height: 14px; background: var(--teal); border-radius: 50%;
    display: inline-block; margin-right: 8px; vertical-align: middle;
  }
  .brand-box__claim { font-size: 32px; color: var(--ink); }
  .product-name {
    position: absolute; left: 0; top: 300px; width: 100%;
    text-align: center; font-size: 70px; color: var(--ink); line-height: 1;
  }
  .strength-box {
    position: absolute; left: 164px; top: 460px; width: 420px; height: 280px;
    background: var(--teal);
    border: 4px solid var(--gold);
    display: flex; align-items: center; justify-content: center;
    text-align: center; color: var(--white);
    font-size: 56px; line-height: 1.05;
  }
  .facts {
    position: absolute; left: 0; top: 770px; width: 100%;
    text-align: center; color: var(--ink);
  }
  .facts__dose { font-size: 50px; line-height: 1; }
  .facts__type { font-size: 26px; letter-spacing: .5px; margin-top: 4px; }
  .facts__volume { font-size: 26px; margin-top: 6px; }
  .facts__flavor { font-size: 27px; margin-top: 22px; }
</style>
</head>
<body>
  <main class="label">
    <div class="label__top" role="img" aria-label="Teal band with faint molecular hexagon pattern"></div>
    <div class="label__bottom" role="img" aria-label="Silver band with faint molecular hexagon pattern"></div>
    <div class="label__rule"></div>

    <div class="brand-box">
      <p class="brand-box__name"><span class="brand-box__mark"></span>Marbleleaf</p>
      <p class="brand-box__claim">Zero THC</p>
    </div>

    <h1 class="product-name" style="font-weight:400">Marbleleaf Hemp</h1>

    <div class="strength-box">
      <p>Premium<br>Full Spectrum<br>2000<br>Hemp Oil</p>
    </div>

    <div class="facts">
      <p class="facts__dose">2000 mg</p>
      <p class="facts__type">DIETARY SUPPLEMENT</p>
      <p class="facts__volume">1FL OZ (30ML)</p>
      <p class="facts__flavor">Natural Peppermint Flavor</p>
    </div>
  </main>
</body>
</html>
```